Presentation Folder for dental clinic

We need a presentation folder design. The presentation folder is what we give to our patients with treatment plans, quotes, images, information sheets etc.
I have uploaded current stationary designs for assistance as well as a photo of our external sign design.
We are an upmarket dental clinic.
Professionalism and customer service is key to us.
We provide information in presentation folders to give to patients.
It needs to memorable and a statement to who we are.

Target Market(s)

Main patient base is Male and Female 40 years old to 70 years old

Industry/Entity Type

Dental Clinic

Font styles to use
Serif
Sans Serif

Requirements
Must have
• Design:
• -Professional
• -Timeless
• -Modern
• - Memorable
• - Statement (if a patient puts down the folder, it will be easily identifiable with as Corvel Dentals folder)
• Logo
• Address, phone, email, website
• Dr Leo Brandt name and degree details
• Colour scheme to match current logos and branding
• "Your Smile Our Passion" quote
Nice to have
• Services listed:
• - Sleep Dentistry
• - Happy Gas
• - Dental Implants
• - Cosmetic Dentistry
• - Oral Surgery
• - Alignora
• - Teeth Whitening
• - General Dentistry
• - Childrens Dentistry
• See website www.corveldental-example.com.au
Should not have
• Dental cliche photos

```html
<!DOCTYPE html>
<html lang="en">
<head>
<meta charset="utf-8">
<title>Corvel Dentals – Presentation Folder</title>
<link href="https://fonts.googleapis.com/css2?family=Lato:wght@400;700&display=swap" rel="stylesheet">
<style>
  :root {
    --purple: #7b3f93;
    --purple-deep: #6a3280;
    --grey: #98979d;
    --grey-light: #eeeef0;
    --paper: #ffffff;
    --paper-inner: #f1f1f1;
    --backdrop: #e4e4e7;
    --ink-light: #ffffff;
    --ink-dark: #3a3a3f;
  }
  * { box-sizing: border-box; margin: 0; padding: 0; }
  html, body { width: 800px; height: 1200px; overflow: hidden; }
  body {
    background: var(--backdrop);
    font-family: "Lato", Arial, sans-serif;
    position: relative;
  }
  .spread {
    position: absolute;
    left: 30px;
    width: 740px;
    height: 500px;
    display: flex;
    box-shadow: 0 6px 18px rgba(0,0,0,.12);
  }
  .spread--outside { top: 50px; }
  .spread--inside { top: 630px; }
  .panel {
    position: relative;
    width: 370px;
    height: 500px;
    background: var(--paper);
    overflow: hidden;
  }
  .band-purple {
    position: absolute;
    left: 0; top: 95px;
    width: 100%; height: 230px;
    background: var(--purple);
    color: var(--ink-light);
  }
  .band-grey {
    position: absolute;
    left: 0; top: 375px;
    width: 100%; height: 125px;
    background: var(--grey);
    color: var(--ink-dark);
  }
  /* back panel */
  .doctor-photo {
    position: absolute;
    left: 12px; top: 12px;
    width: 118px; height: 206px;
    background: linear-gradient(180deg, #eeeeee 0%, #d9d7d5 55%, #5b6270 100%);
    border: 2px solid #f4f4f4;
  }
  .doctor-bio {
    position: absolute;
    left: 144px; top: 12px;
    width: 212px;
    font-size: 7.4px;
    line-height: 1.28;
    text-align: justify;
  }
  .doctor-bio h2 {
    font-size: 10px;
    font-weight: 700;
    margin-bottom: 5px;
  }
  .doctor-bio p + p { margin-top: 6px; }
  .contact-list {
    position: absolute;
    left: 16px; top: 22px;
    list-style: none;
    font-size: 7.6px;
    font-weight: 700;
    color: #2f2f33;
  }
  .contact-list li {
    display: flex;
    align-items: flex-start;
    gap: 6px;
    margin-bottom: 10px;
  }
  .contact-list svg { flex: none; margin-top: 1px; }
  .divider-v {
    position: absolute;
    left: 210px; top: 20px;
    width: 1.5px; height: 78px;
    background: var(--purple);
  }
  .hours {
    position: absolute;
    left: 222px; top: 26px;
    list-style: none;
    font-size: 7.6px;
    font-weight: 700;
    line-height: 1.75;
    color: #2f2f33;
  }
  /* front panel */
  .brand-name {
    position: absolute;
    right: 24px; top: 30px;
    font-size: 34px;
    font-weight: 400;
    letter-spacing: -.5px;
    color: var(--purple);
  }
  .tagline {
    position: absolute;
    left: 14px; top: 90px;
    width: 95px;
    font-size: 18px;
    line-height: 1.3;
    text-align: center;
  }
  .services-rule {
    position: absolute;
    left: 118px; top: 50px;
    width: 1.5px; height: 136px;
    background: var(--ink-light);
  }
  .services {
    position: absolute;
    top: 56px;
    list-style: none;
    font-size: 8.2px;
    line-height: 2.75;
  }
  .services--a { left: 128px; }
  .services--b { left: 248px; top: 50px; }
  .services li::before {
    content: "";
    display: inline-block;
    width: 3px; height: 3px;
    background: var(--ink-light);
    margin-right: 4px;
    vertical-align: middle;
  }
  .grey-cut { position: absolute; left: 0; top: 0; }
  /* inside */
  .panel--inner-left { background: var(--paper-inner); }
  .panel--inner-right { background: #f4f4f4; }
  .pocket { position: absolute; left: 0; bottom: 0; }
</style>
</head>
<body>

<section class="spread spread--outside" aria-label="Folder outside">
  <article class="panel panel--back">
    <div class="band-purple">
      <div class="doctor-photo" role="img" aria-label="Portrait photo of the dentist standing in the clinic"></div>
      <div class="doctor-bio">
        <h2>Dr Leo Brandt</h2>
        <p>Dr Leo Brandt was born and raised in England. He graduated from Westbury College, University of Northfield in 1995. He gained further qualifications in the USA and then worked in general practice in England.<br>
        Dr Leo has advanced training in Intravenous Sedation, Happy Gas, Cosmetic Dentistry, Implants, Bone grafting, Sinus lifts, Oral Surgery and Alignora. All of these multi-skills, enable him to be able to look after and be solely responsible for his patients.</p>
        <p>Outside of dentistry he is a self-confessed sports nut! He plays squash and golf. He is quite a philosophical character and shares this gem with us.<br>
        “Love the job you do, and you never have to work again!”. He feels that he has achieved this with his dentistry, and is enjoying providing excellent care.</p>
        <p>Dr Leo will always, “Do unto others as you would have others do unto you”.</p>
      </div>
    </div>
    <div class="band-grey">
      <ul class="contact-list">
        <li>
          <svg width="7" height="9" viewBox="0 0 7 9"><path d="M3.5 0A3.3 3.3 0 0 0 .2 3.3C.2 5.8 3.5 9 3.5 9s3.3-3.2 3.3-5.7A3.3 3.3 0 0 0 3.5 0zm0 4.6a1.3 1.3 0 1 1 0-2.6 1.3 1.3 0 0 1 0 2.6z" fill="#7b3f93"/></svg>
          <span>41 Harbour Lane, Elmview, VIC, 3999.<br>(Car Park and Reception Entry via Mill Road)</span>
        </li>
        <li>
          <svg width="7" height="7" viewBox="0 0 7 7"><path d="M1.4.2l1 1.5-.6.8a4 4 0 0 0 2.7 2.7l.8-.6 1.5 1-.5 1.2C3.4 6.8.2 3.6.2.7z" fill="#7b3f93"/></svg>
          <span>03 9000 0000</span>
        </li>
        <li>
          <svg width="7" height="7" viewBox="0 0 7 7"><circle cx="3.5" cy="3.5" r="3.3" fill="#7b3f93"/></svg>
          <span>info@corveldental-example.com.au</span>
        </li>
        <li>
          <svg width="7" height="7" viewBox="0 0 7 7"><circle cx="3.5" cy="3.5" r="3.3" fill="#7b3f93"/></svg>
          <span>www.corveldental-example.com.au</span>
        </li>
      </ul>
      <div class="divider-v"></div>
      <ul class="hours">
        <li>Monday 9:00am – 5:00pm</li>
        <li>Tuesday 9:00am – 7:00pm</li>
        <li>Wednesday 9:00am – 1:00pm</li>
        <li>Thursday 9:00am – 5:00pm</li>
        <li>Friday 7:30am – 2:00pm</li>
      </ul>
    </div>
  </article>

  <article class="panel panel--front">
    <div class="brand-name">Corvel Dentals</div>
    <div class="band-purple">
      <p class="tagline">Your Smile Our Passion</p>
      <div class="services-rule"></div>
      <ul class="services services--a">
        <li>Sleep Dentistry</li>
        <li>Cosmetic Dentistry</li>
        <li>General Dentistry</li>
        <li>Alignora</li>
        <li>Oral Surgery</li>
      </ul>
      <ul class="services services--b">
        <li>Happy Gas</li>
        <li>Dental Implants</li>
        <li>Children’s Dentistry</li>
        <li>Teeth Whitening</li>
      </ul>
    </div>
    <div class="band-grey">
      <svg class="grey-cut" width="370" height="125" viewBox="0 0 370 125">
        <polygon points="0,0 140,0 175,125 155,125 120,0" fill="#ffffff" opacity="0"/>
        <polygon points="128,0 140,0 175,125 160,125" fill="#ffffff"/>
      </svg>
    </div>
  </article>
</section>

<section class="spread spread--inside" aria-label="Folder inside">
  <article class="panel panel--inner-left"></article>
  <article class="panel panel--inner-right">
    <svg class="pocket" width="370" height="230" viewBox="0 0 370 230">
      <path d="M0 60 C0 20 30 10 70 10 L370 10 L370 230 L0 230 Z" fill="#ffffff"/>
      <path d="M0 60 C0 20 30 10 70 10 L370 10" fill="none" stroke="#d8d8da" stroke-width="1.5"/>
    </svg>
  </article>
</section>

</body>
</html>
```